M25 Billboard Advert Required Please

I need an advert for a motorway Billboard on the M25 , the advert should show the following in big letters:
GUTTER CLEANING
DALRYNFLUES.COM and a small logo off to the side (Our logo is attached)

The printer has requested the following (Important please) the advert has to be
pdf file / 300 dpi/landscape orientation / scaled to a minimum 25% advert size ( this particular site is 22ft x 10ft so 25% of this please). Please also make sure that the artwork is embedded and outlined correctly if this is incorrect it will affect the printing of the banner.

Target Market(s)

General Public

Industry/Entity Type

Gutter Cleaning

Requirements
Should not have
• No Change to our Logo

```html
<!DOCTYPE html>
<html lang="en">
<head>
<meta charset="UTF-8">
<title>Gutter Cleaning Billboard</title>
<link href="https://fonts.googleapis.com/css2?family=Oswald:wght@500;600;700&family=Open+Sans:wght@600&display=swap" rel="stylesheet">
<style>
  :root {
    --page-bg: #f2f2f2;
    --brand-red: #b41f25;
    --red-glow: #d66a70;
    --sky-top: #ffffff;
    --sky-bottom: #cfe8f6;
    --gutter-light: #a9c6d4;
    --gutter-dark: #5d6b71;
    --cap-grey: #d9dcdc;
    --shirt-green: #4fb784;
    --overall-grey: #4a4f57;
    --headline: #ffffff;
    --ink: #111111;
  }
  * { margin: 0; padding: 0; box-sizing: border-box; }
  html, body { width: 1200px; height: 1200px; overflow: hidden; }
  body { background: var(--page-bg); position: relative; }

  .billboard {
    position: absolute;
    left: 91px; top: 368px;
    width: 1019px; height: 463px;
    overflow: hidden;
  }
  .sky {
    position: absolute; inset: 0;
    background: linear-gradient(180deg, var(--sky-top) 0%, var(--sky-bottom) 100%);
  }
  .gutter-photo {
    position: absolute; left: 0; right: 0; bottom: 0; height: 72px;
    background: linear-gradient(180deg, var(--gutter-light) 0%, #8fa3ab 45%, var(--gutter-dark) 100%);
  }
  .worker-photo {
    position: absolute; left: 700px; top: 45px; width: 300px; bottom: 0;
    border-radius: 120px 120px 0 0;
    background: linear-gradient(180deg,
      var(--cap-grey) 0%, #c9b9a6 22%,
      var(--shirt-green) 38%, #3f9f70 62%,
      var(--overall-grey) 72%, #3a3e45 100%);
  }
  .red-panel { position: absolute; inset: 0; }

  .headline {
    position: absolute; left: 34px;
    font-family: 'Oswald', sans-serif; font-weight: 700;
    color: var(--headline); line-height: 1; white-space: nowrap;
  }
  .headline--main { top: 17px; font-size: 176px; letter-spacing: 13px; }
  .headline--sub { top: 180px; font-size: 118px; letter-spacing: 5px; }
  .web-address {
    position: absolute; left: 34px; top: 308px;
    font-family: 'Oswald', sans-serif; font-weight: 600;
    font-size: 60px; line-height: 1; letter-spacing: 2px;
    color: var(--headline); white-space: nowrap;
  }

  .brand {
    position: absolute; left: 835px; top: 36px;
    font-family: 'Oswald', sans-serif;
  }
  .brand__name {
    display: flex; align-items: center; gap: 8px;
    font-weight: 500; font-size: 22px; line-height: 1; color: var(--ink);
    margin-left: 20px;
  }
  .brand__mark { width: 12px; height: 12px; background: var(--ink); }
  .brand__tagline {
    margin-top: 8px;
    font-family: 'Open Sans', sans-serif; font-weight: 600;
    font-size: 9px; color: var(--ink); white-space: nowrap;
  }
</style>
</head>
<body>
  <section class="billboard">
    <div class="sky"></div>
    <div class="gutter-photo" role="img" aria-label="Close-up of a roof edge and gutter being sprayed with water"></div>
    <div class="worker-photo" role="img" aria-label="Worker in cap, green shirt and grey overalls pressure-washing a roof gutter"></div>

    <svg class="red-panel" viewBox="0 0 1019 463" width="1019" height="463" aria-hidden="true">
      <path d="M754 0 H770 Q612 228 506 391 H487 Q600 220 754 0 Z" fill="var(--red-glow)" opacity="0.85"/>
      <path d="M0 0 H754 Q600 220 487 391 H0 Z" fill="var(--brand-red)"/>
    </svg>

    <h1 class="headline headline--main">GUTTER</h1>
    <h2 class="headline headline--sub">CLEANING</h2>
    <p class="web-address">dalrynflues.com</p>

    <div class="brand">
      <div class="brand__name"><span class="brand__mark"></span>Dalryn Flues</div>
      <p class="brand__tagline">Clean gutters protect your property</p>
    </div>
  </section>
</body>
</html>
```